New Business Card Design For Re-Branded Company (New Logo)

We recently switched our DBA and had a new logo designed. We now need new business cards made around our new logo. We would like to stick with the color scheme in our logo: White, Orange, and Blue. We want to see original bold designs that reflect our position in the solar energy sector but we prefer simple over complicated.

We are curious about vertical designs so if you can translate your design onto a vertical layout we would be open to look at it. We especially like a few designs we have seen on here that are vertical with a black or very dark gray background. They have our logo on one side and then the normal vertical business card on the other side.

I have included a screenshot of one of the samples we like, labeled sample.jpg and a file we were given as an example of our logo on a dark background.

At the same time we are satisfied to stay with what we have always had in a horizontal format. If it's not a lot of extra work for you, designs that are submitted in both horizontal and vertical formats will be greatly appreciated.

Please submit your original, bold, clean designs for consideration. Contact us with any questions or comments that may arise.

Thank you and Good Luck,

KP

```html
<!DOCTYPE html>
<html lang="en">
<head>
<meta charset="utf-8">
<title>Kinetic Power — Business Cards</title>
<link rel="stylesheet" href="https://fonts.googleapis.com/css2?family=Open+Sans:wght@400;600;700&display=swap">
<style>
  :root {
    --bg: #e4e4e2;
    --card-dark: #1e1e1e;
    --orange: #e07a32;
    --blue: #2a7fc1;
    --white: #ffffff;
    --faint-orange: rgba(224, 122, 50, 0.35);
    --faint-white: rgba(255, 255, 255, 0.18);
  }
  * { margin: 0; padding: 0; box-sizing: border-box; }
  html, body { width: 1200px; height: 782px; overflow: hidden; }
  body { background: var(--bg); font-family: "Open Sans", Arial, sans-serif; position: relative; }

  .card { position: absolute; background: var(--card-dark); border-radius: 12px; overflow: hidden; }

  /* Horizontal front */
  .card--front { left: 135px; top: 340px; width: 553px; height: 310px; }
  .front-ring { position: absolute; left: 0; top: 0; }
  .front-brand {
    position: absolute; left: 310px; top: 155px;
    transform: translate(-50%, -50%) rotate(-90deg);
    font-size: 33px; font-weight: 600; letter-spacing: 1px;
    color: var(--orange); white-space: nowrap;
  }
  .front-url {
    position: absolute; left: 513px; top: 155px;
    transform: translate(-50%, -50%) rotate(-90deg);
    font-size: 13px; color: var(--blue); white-space: nowrap;
  }

  /* Vertical back */
  .card--back { left: 710px; top: 84px; width: 326px; height: 568px; }
  .back-mark { position: absolute; left: 0; top: 0; }
  .back-brand {
    position: absolute; left: 0; width: 100%; top: 210px;
    text-align: center; font-size: 22px; font-weight: 600;
    letter-spacing: 1px; color: var(--orange);
  }
  .back-swoosh { position: absolute; left: 0; top: 0; }
  .contact { position: absolute; right: 18px; top: 434px; text-align: right; color: var(--white); }
  .contact__name { font-size: 19px; font-weight: 700; letter-spacing: 0.3px; line-height: 1.2; }
  .contact__title { font-size: 12px; font-weight: 600; letter-spacing: 0.5px; margin-bottom: 12px; }
  .contact__line { font-size: 13px; line-height: 20px; display: flex; justify-content: flex-end; align-items: center; gap: 8px; }
  .contact__line svg { width: 11px; height: 11px; flex: none; }
</style>
</head>
<body>

<section class="card card--front" aria-label="Horizontal card front">
  <svg class="front-ring" width="553" height="310" viewBox="0 0 553 310" aria-hidden="true">
    <circle cx="275" cy="150" r="158" fill="none" stroke="var(--faint-orange)" stroke-width="22"/>
    <circle cx="252" cy="157" r="22" fill="none" stroke="var(--orange)" stroke-width="4"/>
  </svg>
  <div class="front-brand">KINETIC POWER</div>
  <div class="front-url">www.kineticpower.com</div>
</section>

<section class="card card--back" aria-label="Vertical card back">
  <svg class="back-mark" width="326" height="568" viewBox="0 0 326 568" aria-hidden="true">
    <circle cx="163" cy="130" r="62" fill="none" stroke="var(--orange)" stroke-width="8"/>
  </svg>
  <div class="back-brand">KINETIC POWER</div>

  <svg class="back-swoosh" width="326" height="568" viewBox="0 0 326 568" aria-hidden="true">
    <path d="M0 516 C 60 400, 200 320, 326 332 L326 568 L0 568 Z" fill="var(--blue)"/>
    <path d="M0 560 C 50 430, 200 350, 326 350 L326 568 L0 568 Z" fill="var(--orange)"/>
    <circle cx="240" cy="478" r="80" fill="none" stroke="var(--faint-white)" stroke-width="10"/>
  </svg>

  <div class="contact">
    <div class="contact__name">MARLO VENHART</div>
    <div class="contact__title">DIRECTOR</div>
    <div class="contact__line">555 0147 2290
      <svg viewBox="0 0 12 12" aria-hidden="true"><path d="M2.5 1 L4.5 1 L5.3 3.6 L4 4.6 C4.6 6 5.9 7.4 7.4 8 L8.4 6.7 L11 7.5 L11 9.5 C11 10.3 10.3 11 9.5 11 C5 11 1 7 1 2.5 C1 1.7 1.7 1 2.5 1 Z" fill="none" stroke="var(--white)" stroke-width="1"/></svg>
    </div>
    <div class="contact__line">marlo@venhart.com
      <svg viewBox="0 0 12 12" aria-hidden="true"><rect x="1" y="2.5" width="10" height="7" fill="none" stroke="var(--white)" stroke-width="1"/><path d="M1 2.5 L6 6.5 L11 2.5" fill="none" stroke="var(--white)" stroke-width="1"/></svg>
    </div>
    <div class="contact__line">www.kineticpower.com
      <svg viewBox="0 0 12 12" aria-hidden="true"><circle cx="6" cy="6" r="5" fill="none" stroke="var(--white)" stroke-width="1"/><ellipse cx="6" cy="6" rx="2.2" ry="5" fill="none" stroke="var(--white)" stroke-width="1"/><path d="M1 6 H11" stroke="var(--white)" stroke-width="1"/></svg>
    </div>
  </div>
</section>

</body>
</html>
```